Stylish Business Cards Wanted

- DOUBLE SIDED Design Required -

High end, edgy cards for a corporate and personal stylist. Must include logo,
Name: Belinda Forsey
Title: Director and Stylist
telephone : +61 8 8217 4592
email: belinda@thegarbledger.example
website: thegarbledger.example
Tag: Corporate Workwear & Uniform Specialist | Personal Stylist
Would like nice icons for telephone, email, website

Target Market(s)

Businesses wanting stylish uniforms, people wanting stylish wardrobes

Industry/Entity Type

Corporate Workwear Stylist

Contact Information for Business Card

I would like black, white and gold foiling incorporated in the design - possibly a touch of the other colours on my branding guide attached Name: Belinda Forsey Title: Director and Stylist telephone : +61 8 8217 4592 email: belinda@thegarbledger.example website: thegarbledger.example Tag: Corporate Workwear & Uniform Specialist | Personal Stylist Would like nice icons for telephone, email, website

Font styles to use
Other font styles liked:
• Raleway

Colors

Designer to choose colors to be used in the design.

Requirements
Must have
• Gold foil accents

```html
<!DOCTYPE html>
<html lang="en">
<head>
<meta charset="utf-8">
<title>The Garb Ledger — Business Cards</title>
<link rel="stylesheet" href="https://fonts.googleapis.com/css2?family=Montserrat:wght@400;500;700&display=swap">
<style>
  :root {
    --backdrop: #1c1c1c;
    --card-dark: #1f1f1f;
    --card-light: #3a3a3a;
    --gold: #e6bb4a;
    --white: #ffffff;
    --text-soft: #f2f2f2;
  }
  * { box-sizing: border-box; margin: 0; padding: 0; }
  html, body {
    width: 1200px; height: 900px; overflow: hidden;
    background: var(--backdrop);
    font-family: "Montserrat", Arial, sans-serif;
  }
  .canvas {
    position: relative; width: 1200px; height: 900px;
    background: var(--backdrop);
  }
  .card {
    position: absolute; left: 320px; width: 560px; height: 311px;
    background: linear-gradient(225deg, var(--card-light) 0%, var(--card-dark) 55%, var(--card-dark) 100%);
    box-shadow: 0 10px 24px rgba(0,0,0,.55);
  }
  .card--front { top: 110px; }
  .card--back { top: 470px; }

  /* Front */
  .brand-name {
    color: var(--white);
    font-weight: 700;
    letter-spacing: 0.04em;
    line-height: 1;
    white-space: nowrap;
  }
  .card--front .brand-name {
    position: absolute; top: 92px; left: 0; right: 0;
    text-align: center; font-size: 44px;
  }
  .tagline {
    position: absolute; left: 0; right: 0; bottom: 58px;
    text-align: center; color: var(--gold);
    font-size: 12.5px; font-weight: 500; letter-spacing: 0.08em;
  }

  /* Back */
  .card--back .brand-name {
    position: absolute; left: 34px; top: 116px;
    font-size: 30px; width: 200px; white-space: normal;
  }
  .divider {
    position: absolute; left: 244px; top: 70px; width: 1.5px; height: 148px;
    background: var(--gold);
  }
  .contact {
    position: absolute; left: 268px; top: 76px; color: var(--text-soft);
  }
  .contact__name {
    color: var(--gold); font-weight: 700; font-size: 22px;
    letter-spacing: 0.03em; line-height: 1;
  }
  .contact__title {
    font-size: 15px; font-weight: 500; letter-spacing: 0.03em; margin-top: 4px;
  }
  .contact__list { list-style: none; margin-top: 18px; }
  .contact__item {
    display: flex; align-items: center; gap: 10px;
    font-size: 15px; font-weight: 500; letter-spacing: 0.02em;
    line-height: 1; margin-bottom: 9px;
  }
  .contact__icon { width: 14px; height: 14px; flex: none; }
</style>
</head>
<body>
<main class="canvas">

  <section class="card card--front" aria-label="Card front">
    <p class="brand-name">The Garb Ledger</p>
    <p class="tagline">CORPORATE WORKWEAR | UNIFORM SPECIALIST | PERSONAL STYLIST</p>
  </section>

  <section class="card card--back" aria-label="Card back">
    <p class="brand-name">The Garb Ledger</p>
    <div class="divider"></div>
    <div class="contact">
      <p class="contact__name">BELINDA FORSEY</p>
      <p class="contact__title">Director and Stylist</p>
      <ul class="contact__list">
        <li class="contact__item">
          <svg class="contact__icon" viewBox="0 0 24 24" aria-hidden="true">
            <path fill="var(--gold)" d="M6.6 10.8a15.1 15.1 0 0 0 6.6 6.6l2.2-2.2a1 1 0 0 1 1-.25 11.4 11.4 0 0 0 3.6.57 1 1 0 0 1 1 1V20a1 1 0 0 1-1 1A17 17 0 0 1 3 4a1 1 0 0 1 1-1h3.5a1 1 0 0 1 1 1c0 1.25.2 2.45.57 3.57a1 1 0 0 1-.25 1z"/>
          </svg>
          <span>+61 8 8217 4592</span>
        </li>
        <li class="contact__item">
          <svg class="contact__icon" viewBox="0 0 24 24" aria-hidden="true">
            <rect x="2" y="5" width="20" height="14" fill="var(--gold)"/>
            <path d="M2 5l10 8 10-8" fill="none" stroke="var(--card-dark)" stroke-width="1.6"/>
          </svg>
          <span>belinda@thegarbledger.example</span>
        </li>
        <li class="contact__item">
          <svg class="contact__icon" viewBox="0 0 24 24" aria-hidden="true">
            <circle cx="12" cy="12" r="10" fill="var(--gold)"/>
            <path d="M2 12h20M12 2c3 3 3 17 0 20M12 2c-3 3-3 17 0 20" fill="none" stroke="var(--card-dark)" stroke-width="1.4"/>
          </svg>
          <span>www.thegarbledger.example</span>
        </li>
      </ul>
    </div>
  </section>

</main>
</body>
</html>
```